Squarespace website build: Quirk literary annual (initial design work supplied)

Our brand guidelines provide the look and feel for the website - we just need someone to create it based on our mock ups!
PLEASE NOTE:
- Please base our website off the website pages within the brief (ie homepage is GREEN)
- please ensure each page will be standalone (not a scrolling home page)
- please only use filtered duotone style photography as a hold, if you think the page needs a photo.
-please not the websites i have provided as an influence - especially TIDE YEARLY. We want very little photography.

Quirk is a literary and arts journal that provides a platform for both emerging and established writers and artists from New Zealand and beyond. We are passionate about sharing insights into the intimate and unique worlds of creatives with short stories, poetry, and art – showcasing raw and unfiltered glimpses into their world.

We have our brand guidelines and logo finalised, with a 'look and feel' design for the website within our attached brand guidelines document. We just need someone to design this simple website on Squarespace for us. It will have five pages and will need a newsletter sign up link:
Home page
About us page
Submissions page
Purchase page
Contact page

DRAFT WEB COPY

ABOUT
QUIRK is an independent literary annual journal established in 2022 by Hazel Wintergate and Mereana Clift that publishes unrepentant unfiltered accounts of life, eclectic takes on the mundane ordinary, and deep dives into modern love & sexuality.
Founder, Editor: Hazel Arohanui Wintergate
Founder, Production Director: Mereana Clift
Art Direction: Lorna Pike
Editorial Assistant: Kirsten Holloway-Dunn

I suggest duotone fashion-esque photography which is very Vesna Kordell/ Palm Springs vibe but not obviously identifiable.
· I love the style of Rufus Tennick for our shoot in particular. Group lazing around a pool, leisurely, glam, but effortless and ironically looking very natural – as though – yes, these are our lives.
SUBMISSION PAGE
Quirk welcomes submissions all year round.
We are drawn to dark humour, satirical takes on the social scene, and starkly honest accounts of ordinary life. Diversity is celebrated, adversity is welcomed and, above all, personal expression is championed. We are particularly seeking content that takes risks, screams of honesty and celebrates life’s most extraordinary moments.
Selected works will be published in our annual publication.

Submission guidelines
We accept flash fiction, short stories and poetry. Individual entries not to mustn’t exceed 2000 words.
Submitted work must be unpublished and in English. We welcome simultaneous submissions, but must be notified immediately if your manuscript is accepted for publication elsewhere or appears in any print or online source. We will endeavour to respond to all submissions within four weeks.
Please send submissions as a word document along with a brief bio of 50 words to pages@quirkjournal.test
PO Box[EB2]
​Note on Copyright: Copyright remains with the author.

Annual short story competition
Volume Alpha is interested in all that is spiritual, coincidental, or mysterious. Stories selected for this issue reflect life’s uncanny moments, those that defy explanation, and experiences that promote personal and spiritual growth. Entires must be no longer than 2000 words.

First prize: 1000
Second prize: 500
Third prize: 200[EB3]

SUPPORT US
Since our launch in 2022, we have relied upon the generous support of our creative business community in Wellington City, New Zealand. If you read us, or love our ethos, please consider a donation.
Link to chipinhere page
Updates

Hello designers
I would ideally love to have someone turn this around within a few weeks, because the design work has mostly been provided.
Thanks
Hazel

Hi everyone Please ensure you read our brand guidelines and follow the brief. Please note we do not yet have a product, as this is a new venture, so there is no point including images of a magazine that doesn't yet exist. Some further comment to ensure we get there: - We want all pages to be separate pages (not a scrolling home page) with a different colour based on the guidelines - The home page must look just as it does in the brand guidelines - There is no archive page (please read brief) as we have no archive yet. The pages are: Home, About, Contact, Competitions and submissions Thank you

Target Market(s)

writers and creatives

Industry/Entity Type

Writing/ creative/ publishing

Coding

Coded - Design and coding required

Number of Pages Required

4 page

Font styles to use
Other font styles liked:
• COTTA and Univers - as per brand guidelines

Requirements
Must have
• Squarespace designer needed to design our mocked up webpages.
Nice to have
• As close to the brand guideline mock ups as possible (see page 11,12,13)
Should not have
• anything outside of the brand guidelines

```html
<!DOCTYPE html>
<html lang="en">
<head>
<meta charset="utf-8">
<title>Quirk — literary annual</title>
<link rel="stylesheet" href="https://fonts.googleapis.com/css2?family=Marcellus&family=Roboto+Condensed:wght@300;400;700&display=swap">
<style>
:root{
  --green:#647733;
  --mustard:#b9a026;
  --yellow:#c9ad1d;
  --gold:#bfa534;
  --pink:#c5587a;
  --pink-deep:#b94a70;
  --purple:#693e66;
  --cream:#efe9de;
  --light:#f4efe2;
  --display:"Marcellus", Georgia, serif;
  --body:"Roboto Condensed", "Arial Narrow", sans-serif;
}
*{box-sizing:border-box;margin:0;padding:0}
html,body{width:1200px;height:3867px;overflow:hidden}
body{position:relative;background:var(--green);color:var(--light);font-family:var(--body);font-weight:300}
.abs{position:absolute}
.center{left:0;width:1200px;text-align:center}

/* header */
.nav{top:42px;left:110px;display:flex;gap:20px;font-size:15px;font-weight:400;letter-spacing:.3px}
.nav a{color:var(--light);text-decoration:none;position:relative}
.nav a.active::after{content:"";position:absolute;left:0;right:0;bottom:-9px;height:2px;background:var(--pink)}
.brand{top:18px;left:0;width:1200px;text-align:center;font-family:var(--display);font-size:64px;color:var(--gold);line-height:1}
.contact-btn{top:35px;left:969px;width:120px;height:49px;background:var(--purple);color:var(--light);font-size:15px;font-weight:700;display:flex;align-items:center;justify-content:center;letter-spacing:.5px}

/* hero */
.hero-title{top:148px;font-family:var(--display);font-size:45px;line-height:51px;color:var(--light)}
.hero-title .mark{position:relative}
.hero-title .mark::after{content:"";position:absolute;left:0;right:0;bottom:-6px;height:3px;background:var(--pink)}
.hero-frame{top:357px;left:234px}
.hero-photo{top:377px;left:252px;width:696px;height:640px;background:linear-gradient(160deg,#d97b99 0%,#c9567b 45%,#a8355e 100%)}

/* about */
h2.section-title{font-family:var(--display);font-weight:400;font-size:42px;letter-spacing:1px;color:var(--light)}
.about-title{top:1118px}
.about-copy{top:1208px;left:150px;width:900px;text-align:center;font-size:20px;line-height:30px}
.credits{left:0;width:1200px;text-align:center;font-size:20px}
.credits b{font-weight:700}

/* submission band */
.band-sub{top:1553px;left:0;width:1200px;height:448px;background:var(--mustard)}
.sub-title{top:1622px}
.sub-lead{top:1700px;font-size:22px}
.sub-copy{top:1750px;left:145px;width:910px;text-align:center;font-size:20px;line-height:30px}
.sub-note{top:1898px;font-size:22px}

/* cards */
.photo-pink{top:2074px;left:111px;width:488px;height:586px;background:radial-gradient(circle at 62% 50%,#8e2c4d 0 12%,#d07b98 13% 40%,#c2577b 70%,#b24a6e 100%)}
.photo-purple{top:2743px;left:599px;width:490px;height:528px;background:linear-gradient(170deg,#8d5a88 0%,#7b4c77 55%,#6e4069 100%)}
.cover{background:var(--cream)}
.cover-art{background:linear-gradient(180deg,#d0b428,#b89c1c)}
.cover-name{font-family:var(--display);text-align:center;line-height:1}
.panel{background:var(--cream);color:#3b3b2e;padding:46px 47px;font-size:19.5px;line-height:30px;font-weight:400}
.panel h3{font-family:var(--body);font-weight:700;color:var(--green);font-size:23px;line-height:30px;margin-bottom:18px}
.panel p{margin-bottom:6px;text-align:justify}
.panel .hl{color:var(--pink-deep);font-weight:700}
.panel-guides{top:2118px;left:545px;width:445px;height:435px}
.panel-comp{top:2786px;left:203px;width:443px;height:323px}

/* support */
.band-support{top:3345px;left:0;width:1200px;height:332px;background:linear-gradient(90deg,#cfb21c 0%,#c7aa17 55%,#c09e12 100%)}
.support-title{top:3392px}
.support-copy{top:3470px;left:150px;width:900px;text-align:center;font-size:20px;line-height:30px}
.donate{top:3567px;left:540px;width:119px;height:48px;background:var(--cream);color:var(--green);font-weight:700;font-size:14px;display:flex;align-items:center;justify-content:center;letter-spacing:.5px}

/* footer */
.footer-brand{top:3718px;left:110px;font-family:var(--display);font-size:66px;color:var(--light);line-height:1}
.footer-info{left:416px;font-size:16px;font-weight:400}
.social{top:3812px;width:31px;height:31px;border:1.5px solid var(--light);border-radius:50%}
.touch{left:1008px;font-size:16px;font-weight:400}
.touch-head{font-weight:700}
</style>
</head>
<body>

<header>
  <nav class="abs nav">
    <a class="active">HOME</a><a>ABOUT</a><a>SUBMISSIONS</a><a>PURCHASE</a>
  </nav>
  <div class="abs brand">quirk</div>
  <div class="abs contact-btn">CONTACT</div>
</header>

<section class="hero">
  <h1 class="abs center hero-title" style="font-weight:400">Quirk is a plucky little publication<br>out of Wellington, New Zealand -<br>give it a read <span class="mark">here</span></h1>
  <svg class="abs hero-frame" width="730" height="679" viewBox="0 0 730 679" fill="none" stroke="#b59c2e" stroke-width="1.5" aria-hidden="true">
    <path d="M48 0 H682 V20 H696 V48 H716 V631 H696 V659 H682 V679 H48 V659 H34 V631 H14 V48 H34 V20 H48 Z"/>
    <path d="M2 14 H28 V36 M0 30 H14 V20"/>
    <path d="M728 14 H702 V36 M730 30 H716 V20"/>
    <path d="M2 665 H28 V643 M0 649 H14 V659"/>
    <path d="M728 665 H702 V643 M730 649 H716 V659"/>
  </svg>
  <div class="abs hero-photo" role="img" aria-label="Pink duotone fashion portrait in a city street"></div>
</section>

<section class="about">
  <h2 class="abs center section-title about-title">ABOUT US</h2>
  <p class="abs about-copy">QUIRK is an independent literary annual journal established in 2022 by Hazel Wintergate and Mereana Clift that publishes unrepentant unfiltered accounts of life, eclectic takes on the mundane ordinary, and deep dives into modern love &amp; sexuality.</p>
  <p class="abs credits" style="top:1318px">Founder, Editor: <b>Hazel Arohanui Wintergate</b></p>
  <p class="abs credits" style="top:1360px">Founder, Production Director: <b>Mereana Clift</b></p>
  <p class="abs credits" style="top:1403px">Art Direction: <b>Lorna Pike</b></p>
  <p class="abs credits" style="top:1446px">Editorial Assistant: <b>Kirsten Holloway-Dunn</b></p>
</section>

<section>
  <div class="abs band-sub"></div>
  <h2 class="abs center section-title sub-title">SUBMISSION</h2>
  <p class="abs center sub-lead">Quirk welcomes submissions all year round.</p>
  <p class="abs sub-copy">We are drawn to dark humour, satirical takes on the social scene, and starkly honest accounts of ordinary life. Diversity is celebrated, adversity is welcomed and, above all, personal expression is championed. We are particularly seeking content that takes risks, screams of honesty and celebrates life’s most extraordinary moments.</p>
  <p class="abs center sub-note">Selected works will be published in our annual publication.</p>
</section>

<section class="cards">
  <div class="abs photo-pink" role="img" aria-label="Pink duotone spiral staircase"></div>
  <div class="abs cover" style="top:2331px;left:120px;width:240px;height:320px">
    <div class="cover-name" style="margin-top:18px;font-size:54px;color:var(--green)">quirk</div>
    <div class="abs cover-art" style="top:110px;left:18px;width:204px;height:210px" role="img" aria-label="Journal cover portrait in yellow duotone"></div>
  </div>
  <div class="abs panel panel-guides">
    <h3>SUBMISSION GUIDELINES</h3>
    <p>We accept flash fiction, short stories and poetry. Individual entries not to mustn’t exceed 2000 words</p>
    <p style="margin-bottom:0">Please send submissions as a word document along with a brief bio of 50 words to<br><span class="hl">pages@quirkjournal.test</span><br><span class="hl">PO Box[EB2]</span><br>Note on Copyright: Copyright remains with the author.</p>
  </div>

  <div class="abs photo-purple" role="img" aria-label="Purple duotone portrait of a reader in glasses"></div>
  <div class="abs cover" style="top:2943px;left:838px;width:242px;height:324px;background:var(--yellow)">
    <div class="cover-name" style="margin-top:18px;font-size:54px;color:#9c8520">quirk</div>
    <div class="abs" style="top:108px;left:18px;width:206px;height:212px;background:linear-gradient(180deg,#6d8036,#566a27)" role="img" aria-label="Journal cover portrait in green duotone"></div>
  </div>
  <div class="abs panel panel-comp">
    <h3>ANNUAL SHORT STORY<br>COMPETITION</h3>
    <p style="margin-bottom:0">Entires must be no longer than 2000 words.<br>First prize: <span class="hl">1000</span><br>Second prize: <span class="hl">500</span><br>Third prize: <span class="hl">200[EB3]</span></p>
  </div>
</section>

<section>
  <div class="abs band-support" role="img" aria-label="Yellow duotone photo of friends laughing"></div>
  <h2 class="abs center section-title support-title">SUPPORT US</h2>
  <p class="abs support-copy">Since our launch in 2022, we have relied upon the generous support of our creative business community in Wellington City, New Zealand. If you read us, or love our ethos, please consider a donation.</p>
  <div class="abs donate">DONATE</div>
</section>

<footer>
  <div class="abs footer-brand">quirk</div>
  <p class="abs footer-info" style="top:3735px">Quirk is a publication out of Wellington, New Zealand</p>
  <p class="abs footer-info" style="top:3770px">2022 Quirk. All Rights Reserved.</p>
  <span class="abs social" style="left:416px" aria-label="Social link"></span>
  <span class="abs social" style="left:463px" aria-label="Social link"></span>
  <p class="abs touch touch-head" style="top:3731px">Get in Touch</p>
  <p class="abs touch" style="top:3771px">Email</p>
  <p class="abs touch" style="top:3798px">Sign up</p>
  <p class="abs touch" style="top:3826px">Newsletter</p>
</footer>

</body>
</html>
```